Web design for insurance consultant. Target clients are (re)insurers, insurtech firms and vendor...

Need a crisp, modern website which will talk briefly about the firm and its principal founder. And, details around services offered for 3 different target clients: (1) re/insurance companies, (2) insurtech and IoT firms, and (3) vendors such as claims adjusting firms and home inspection firms supporting insurers

Target Market(s)

C-suite leaders of insurance companies, reinsurance companies, insurtech firms looking to innovate property insurance, and vendors selling to these insurance companies. Focus is property insurance in coastal, catastrophe-exposed regions of the US.

Coding

Coded - Design and coding required

Number of Pages Required

5+ page

Other font styles liked:
• not sure of font wanted - classic, but modern

Colors
0792cd
00a990

Requirements
Must have
• First box should use the attached "light bulb storm" picture as background.
• one change overall - remove "Get a quote" button - we do not sell to consumers, it's strictly B2B.
• For the 3 segments, use the pictures below. I could not find one I liked for "TPAs/Vendors", so welcome your suggestions.
• Want quotes in the boxes of each of the 3 market segments.
• Button on each of the 3 market segments would lead to content (not yet finished) that will explain in more detail the services to be provided to them.
Should not have
• don't want google maps or others showing location of business (waste of space, in my opinion)

```html
<!DOCTYPE html>
<html lang="en">
<head>
<meta charset="utf-8">
<title>halden consulting</title>
<link href="https://fonts.googleapis.com/css2?family=Catamaran:wght@500;600;700&family=Questrial&display=swap" rel="stylesheet">
<style>
:root{
  --blue:#1b5c98;
  --green:#6fa31a;
  --dark:#121417;
  --ink:#3d4148;
  --muted:#6c7078;
  --light:#f3f3f3;
  --white:#ffffff;
  --line:#d9d9d9;
}
*{box-sizing:border-box;margin:0;padding:0}
html,body{width:1200px;height:3659px;overflow:hidden;background:var(--white)}
body{font-family:"Questrial",Arial,sans-serif;color:var(--ink)}
.page{position:relative;width:1200px;height:3659px;overflow:hidden}
.abs{position:absolute}
.heading{font-family:"Catamaran",Arial,sans-serif;font-weight:600;font-size:42px;text-align:center;color:var(--blue);letter-spacing:-.3px}
.heading span{color:var(--green)}
.center{left:0;width:1200px;text-align:center}

/* header + hero */
.hero{left:0;top:0;width:1200px;height:745px;background:linear-gradient(160deg,#3d3a36 0%,#5a5650 35%,#2b2c30 70%,#1d1f23 100%)}
.hero-shade{left:0;top:0;width:1200px;height:745px;background:rgba(10,12,16,.45)}
.nav-bar{left:0;top:0;width:1200px;height:105px;background:rgba(0,0,0,.82)}
.brand{left:78px;top:30px;display:flex;align-items:center;gap:12px;color:var(--white);font-family:"Catamaran",Arial,sans-serif;font-weight:600;font-size:30px;line-height:1}
.brand-dot{width:46px;height:46px;border-radius:50%;background:var(--green)}
.nav{right:78px;top:30px;display:flex;gap:22px;align-items:center}
.nav a{font-family:"Questrial",Arial,sans-serif;font-size:15px;color:var(--white);text-decoration:none;padding:10px 14px;border-radius:24px;letter-spacing:.3px}
.nav a.active{border:2px solid var(--green);color:var(--green)}
.hero-ring{left:534px;top:276px;width:132px;height:132px;border-radius:50%;border:3px solid rgba(255,255,255,.8);background:rgba(0,0,0,.15)}
.hero-ring::after{content:"";position:absolute;left:26px;top:26px;width:74px;height:74px;border-radius:50%;background:var(--green)}
.hero-title{top:425px;font-family:"Catamaran",Arial,sans-serif;font-weight:600;font-size:60px;color:var(--white)}
.hero-sub{top:510px;font-size:18px;color:var(--white)}
.hero-curve{left:0;top:600px}

/* welcome */
.welcome-title{top:795px}
.welcome-text{left:300px;top:862px;width:600px;text-align:center;font-size:13.5px;line-height:26px;color:var(--muted)}
.welcome-text p+p{margin-top:14px}
.btn{display:inline-block;background:var(--green);color:var(--white);font-family:"Catamaran",Arial,sans-serif;font-weight:600;font-size:20px;text-align:center}
.know-more{left:517px;top:1030px;width:166px;height:48px;line-height:50px}

/* services */
.services{left:0;top:1166px;width:1200px;height:793px;background:linear-gradient(120deg,#15171b 0%,#2d2e31 40%,#3c3b39 60%,#18191c 100%)}
.services-shade{left:0;top:1166px;width:1200px;height:793px;background:rgba(8,10,14,.55)}
.services-title{top:1212px}
.seg-name{font-size:19px;color:var(--white)}
.seg-quote{font-size:13.5px;line-height:24px;color:#e6e6e6}
.read-more{font-size:13px;color:var(--white);text-decoration:underline;display:flex;align-items:center;gap:12px;letter-spacing:.5px}
.read-more svg{display:block}
.seg-top-name{top:1292px}
.seg-top-quote{left:450px;top:1330px;width:300px;text-align:center}
.seg-top-link{left:537px;top:1420px}
.seg-left-name{left:78px;top:1492px}
.seg-left-quote{left:78px;top:1562px;width:250px}
.seg-left-link{left:78px;top:1654px}
.seg-right-name{left:878px;top:1492px;width:244px;text-align:right}
.seg-right-quote{left:878px;top:1562px;width:244px;text-align:right}
.seg-right-link{left:998px;top:1654px}
.node{border-radius:50%;background:var(--white);display:flex;align-items:center;justify-content:center}
.node-top{left:537px;top:1476px;width:126px;height:126px}
.node-left{left:342px;top:1620px;width:126px;height:126px}
.node-right{left:730px;top:1620px;width:126px;height:126px}
.node-hub{left:488px;top:1625px;width:224px;height:224px;flex-direction:column;gap:6px}
.hub-name{font-family:"Catamaran",Arial,sans-serif;font-weight:600;font-size:30px;color:var(--blue)}
.hub-dot{width:18px;height:18px;border-radius:50%;background:var(--green)}

/* testimonials */
.testimonials{left:0;top:1959px;width:1200px;height:561px;background:var(--light)}
.testimonials-title{top:2003px}
.card{top:2081px;width:239px;height:354px;background:var(--white);box-shadow:0 2px 10px rgba(0,0,0,.08);text-align:center}
.avatar{position:absolute;left:68px;top:44px;width:103px;height:103px;border-radius:50%;border:3px solid var(--green)}
.avatar-fill{position:absolute;inset:4px;border-radius:50%}
.card-name{position:absolute;left:0;top:174px;width:100%;font-size:19px;color:var(--blue)}
.card-text{position:absolute;left:20px;top:212px;width:199px;font-size:13px;line-height:25px;color:var(--muted)}

/* call band */
.band{left:0;top:2520px}
.call-label{left:78px;top:2568px;font-family:"Catamaran",Arial,sans-serif;font-weight:600;font-size:28px;color:var(--white);display:flex;align-items:center;gap:22px}
.call-icon{width:54px;height:54px;border-radius:50%;border:2px solid var(--white);display:flex;align-items:center;justify-content:center}
.call-number{font-size:29px}
.band-text{left:650px;top:2562px;width:340px;text-align:center;font-size:13.5px;line-height:26px;color:var(--white)}
.join-us{left:1017px;top:2566px;width:105px;height:46px;line-height:48px;background:var(--blue);font-size:20px}

/* news */
.news-title{top:2700px}
.news-card{top:2776px;width:322px;height:427px;background:var(--light)}
.news-photo{position:absolute;left:0;top:0;width:322px;height:208px}
.news-date{position:absolute;left:0;top:0;width:50px;height:70px;background:var(--green);color:var(--white);text-align:center;font-family:"Catamaran",Arial,sans-serif;font-weight:600}
.news-day{display:block;font-size:27px;line-height:30px;margin-top:9px}
.news-month{display:block;font-size:12px;line-height:14px}
.news-head{position:absolute;left:22px;top:242px;width:290px;font-size:17px;line-height:30px;color:var(--ink)}
.news-body{position:absolute;left:22px;top:314px;width:280px;font-size:13px;line-height:24px;color:var(--muted)}

/* footer */
.footer{left:0;top:3293px;width:1200px;height:366px;background:linear-gradient(180deg,#16181b 0%,#1e2024 60%,#14161a 100%)}
.f-node{top:3369px;width:108px;height:108px;border-radius:50%;border:4px solid rgba(111,163,26,.45);display:flex;align-items:center;justify-content:center}
.f-node-inner{width:90px;height:90px;border-radius:50%;background:var(--green);display:flex;align-items:center;justify-content:center}
.f-text{top:3502px;font-size:13.5px;line-height:25px;color:var(--white);text-align:center}
.f-dots{top:3423px;height:0;border-top:2px dotted rgba(255,255,255,.35)}
.copyright{top:3596px;font-size:13px;color:#d0d0d0}
</style>
</head>
<body>
<div class="page">

  <!-- hero -->
  <div class="abs hero" role="img" aria-label="Photo of two colleagues working together at a laptop in an office"></div>
  <div class="abs hero-shade"></div>
  <div class="abs nav-bar"></div>
  <div class="abs brand"><span class="brand-dot"></span>halden consulting</div>
  <nav class="abs nav">
    <a class="active" href="#">HOME</a>
    <a href="#">ABOUT</a>
    <a href="#">SERVICES</a>
    <a href="#">NEWS</a>
    <a href="#">CONTACT</a>
  </nav>
  <div class="abs hero-ring"></div>
  <h1 class="abs center hero-title">halden consulting</h1>
  <p class="abs center hero-sub">Lorem Ipsum is simply dummy text of the printing and typesetting.</p>
  <svg class="abs hero-curve" width="1200" height="150" viewBox="0 0 1200 150" aria-hidden="true">
    <path d="M0 60 C300 140 720 165 1200 10 L1200 150 L0 150 Z" fill="#ffffff"/>
  </svg>

  <!-- welcome -->
  <h2 class="abs center heading welcome-title">welcome to <span>halden consulting</span></h2>
  <div class="abs welcome-text">
    <p>Lorem Ipsum is simply dummy text of the printing and typesetting industry. Lorem Ipsum has been the industry's standard dummy text ever since the 1500s, when an unknown printer took a galley of type and scrambled it to make a type specimen book.</p>
    <p>It has survived not only five centuries, but also the leap into electronic typesetting, remaining essentially unchanged. It was popularised in the 1960s with the release.</p>
  </div>
  <a class="abs btn know-more">know more</a>

  <!-- services -->
  <div class="abs services" role="img" aria-label="Photo of a businesswoman on the phone in front of a laptop"></div>
  <div class="abs services-shade"></div>
  <h2 class="abs center heading services-title" style="color:#2a7cc0">services <span>we provide</span></h2>

  <svg class="abs" style="left:0;top:1166px" width="1200" height="793" viewBox="0 0 1200 793" aria-hidden="true">
    <g stroke="#ffffff" stroke-width="1.5" fill="none">
      <line x1="78" y1="373" x2="317" y2="373"/>
      <line x1="317" y1="373" x2="370" y2="470"/>
      <line x1="878" y1="373" x2="1122" y2="373"/>
      <line x1="878" y1="373" x2="826" y2="470"/>
      <line x1="600" y1="436" x2="600" y2="460"/>
      <line x1="450" y1="565" x2="500" y2="610"/>
      <line x1="750" y1="565" x2="700" y2="610"/>
    </g>
  </svg>

  <div class="abs center seg-name seg-top-name">Vendors and TPAs</div>
  <p class="abs seg-quote seg-top-quote">"Halden knows everybody in this space. As important as his connections were to us, he also provided huge value...</p>
  <a class="abs read-more seg-top-link">READ MORE <svg width="26" height="12" viewBox="0 0 26 12"><path d="M0 6H24M19 1l5 5-5 5" stroke="#fff" stroke-width="1.8" fill="none"/></svg></a>

  <div class="abs seg-name seg-left-name">(Re)Insurers</div>
  <p class="abs seg-quote seg-left-quote">"Halden has a unique skill set in property cat that helped us refine our approach, particularly...</p>
  <a class="abs read-more seg-left-link">READ MORE <svg width="26" height="12" viewBox="0 0 26 12"><path d="M0 6H24M19 1l5 5-5 5" stroke="#fff" stroke-width="1.8" fill="none"/></svg></a>

  <div class="abs seg-name seg-right-name">Insurtech / IoT</div>
  <p class="abs seg-quote seg-right-quote">"We didn't realize how hard insurance is... Sam's operational insights and suggestions...</p>
  <a class="abs read-more seg-right-link">READ MORE <svg width="26" height="12" viewBox="0 0 26 12"><path d="M0 6H24M19 1l5 5-5 5" stroke="#fff" stroke-width="1.8" fill="none"/></svg></a>

  <div class="abs node node-top">
    <svg width="54" height="54" viewBox="0 0 54 54" aria-label="balance icon"><circle cx="27" cy="27" r="24" fill="none" stroke="#1b5c98" stroke-width="4"/><path d="M27 3a24 24 0 0 1 0 48a12 12 0 0 1 0-24a12 12 0 0 0 0-24z" fill="#1b5c98"/><circle cx="27" cy="15" r="4" fill="#fff"/><circle cx="27" cy="39" r="4" fill="#1b5c98"/></svg>
  </div>
  <div class="abs node node-left">
    <svg width="56" height="56" viewBox="0 0 56 56" aria-label="protected person icon"><circle cx="18" cy="12" r="7" fill="#1b5c98"/><path d="M6 50V30a8 8 0 0 1 8-8h8a8 8 0 0 1 8 8v20h-6V36h-2v14H14V36h-2v14z" fill="#1b5c98"/><path d="M40 24l12 4v9c0 8-5 13-12 16c-7-3-12-8-12-16v-9z" fill="#1b5c98"/></svg>
  </div>
  <div class="abs node node-right">
    <svg width="56" height="56" viewBox="0 0 56 56" aria-label="globe icon"><g fill="none" stroke="#1b5c98" stroke-width="3.5"><circle cx="28" cy="28" r="23"/><ellipse cx="28" cy="28" rx="10" ry="23"/><line x1="5" y1="28" x2="51" y2="28"/><path d="M9 16h38M9 40h38"/></g></svg>
  </div>
  <div class="abs node node-hub"><span class="hub-dot"></span><span class="hub-name">halden</span></div>

  <!-- testimonials -->
  <div class="abs testimonials"></div>
  <h2 class="abs center heading testimonials-title">client <span>testimonials</span></h2>

  <div class="abs card" style="left:78px">
    <div class="avatar"><div class="avatar-fill" role="img" aria-label="Client portrait" style="background:linear-gradient(160deg,#8a6a52,#c9a58a)"></div></div>
    <div class="card-name">- name surname</div>
    <p class="card-text">Lorem Ipsum is simply dummy text of the printing and typesetting industry. Lorem Ipsum has been the industry.</p>
  </div>
  <div class="abs card" style="left:346px">
    <div class="avatar"><div class="avatar-fill" role="img" aria-label="Client portrait" style="background:linear-gradient(160deg,#b08a66,#e2c7ad)"></div></div>
    <div class="card-name">- name surname</div>
    <p class="card-text">Lorem Ipsum is simply dummy text of the printing and typesetting industry. Lorem Ipsum has been the industry.</p>
  </div>
  <div class="abs card" style="left:614px">
    <div class="avatar"><div class="avatar-fill" role="img" aria-label="Client portrait" style="background:linear-gradient(160deg,#4a5a44,#9a8f7c)"></div></div>
    <div class="card-name">- name surname</div>
    <p class="card-text">Lorem Ipsum is simply dummy text of the printing and typesetting industry. Lorem Ipsum has been the industry.</p>
  </div>
  <div class="abs card" style="left:883px">
    <div class="avatar"><div class="avatar-fill" role="img" aria-label="Client portrait" style="background:linear-gradient(160deg,#3b4a5e,#a0907e)"></div></div>
    <div class="card-name">- name surname</div>
    <p class="card-text">Lorem Ipsum is simply dummy text of the printing and typesetting industry. Lorem Ipsum has been the industry.</p>
  </div>

  <!-- call band -->
  <svg class="abs band" width="1200" height="137" viewBox="0 0 1200 137" aria-hidden="true">
    <polygon points="0,0 552,0 586,137 0,137" fill="#1b5c98"/>
    <polygon points="567,0 1200,0 1200,137 601,137" fill="#6fa31a"/>
  </svg>
  <div class="abs call-label">call us on
    <span class="call-icon"><svg width="26" height="26" viewBox="0 0 24 24"><path d="M6.6 10.8a15.2 15.2 0 0 0 6.6 6.6l2.2-2.2a1 1 0 0 1 1-.25 11.4 11.4 0 0 0 3.6.57 1 1 0 0 1 1 1V20a1 1 0 0 1-1 1A17 17 0 0 1 3 4a1 1 0 0 1 1-1h3.5a1 1 0 0 1 1 1c0 1.25.2 2.45.57 3.6a1 1 0 0 1-.25 1z" fill="#fff"/></svg></span>
    <span class="call-number">123 456 7890</span>
  </div>
  <p class="abs band-text">Lorem Ipsum is simply dummy text of the printing and typesetting industry Lorem Ipsum has been.</p>
  <a class="abs btn join-us">join us</a>

  <!-- news -->
  <h2 class="abs center heading news-title">latest <span>news</span></h2>

  <div class="abs news-card" style="left:78px">
    <div class="news-photo" role="img" aria-label="Photo of two people reviewing documents at a laptop" style="background:linear-gradient(135deg,#d9cdb8,#a58c6a 60%,#6b5a46)"></div>
    <div class="news-date"><span class="news-day">15</span><span class="news-month">SEP</span></div>
    <p class="news-head">Lorem Ipsum is simply dummy text of the printing and typesetting.</p>
    <p class="news-body">Lorem Ipsum is simply dummy text of the printing and typesetting industry. Lorem Ipsum has been the industry's standard du.</p>
  </div>
  <div class="abs news-card" style="left:439px">
    <div class="news-photo" role="img" aria-label="Photo of a smiling man working at a laptop in an office" style="background:linear-gradient(135deg,#c9b79d,#8d7a62 55%,#4c4238)"></div>
    <div class="news-date"><span class="news-day">15</span><span class="news-month">SEP</span></div>
    <p class="news-head">Lorem Ipsum is simply dummy text of the printing and typesetting.</p>
    <p class="news-body">Lorem Ipsum is simply dummy text of the printing and typesetting industry. Lorem Ipsum has been the industry's standard du.</p>
  </div>
  <div class="abs news-card" style="left:800px">
    <div class="news-photo" role="img" aria-label="Photo of a team meeting around a conference table" style="background:linear-gradient(135deg,#c8d0d6,#7d8c98 55%,#3e4852)"></div>
    <div class="news-date"><span class="news-day">15</span><span class="news-month">SEP</span></div>
    <p class="news-head">Lorem Ipsum is simply dummy text of the printing and typesetting.</p>
    <p class="news-body">Lorem Ipsum is simply dummy text of the printing and typesetting industry. Lorem Ipsum has been the industry's standard du.</p>
  </div>

  <!-- footer -->
  <div class="abs footer" role="img" aria-label="Dark photo of a laptop on a desk"></div>
  <div class="abs f-dots" style="left:320px;width:200px"></div>
  <div class="abs f-dots" style="left:680px;width:200px"></div>

  <div class="abs f-node" style="left:185px"><div class="f-node-inner">
    <svg width="30" height="30" viewBox="0 0 24 24" aria-label="phone"><path d="M6.6 10.8a15.2 15.2 0 0 0 6.6 6.6l2.2-2.2a1 1 0 0 1 1-.25 11.4 11.4 0 0 0 3.6.57 1 1 0 0 1 1 1V20a1 1 0 0 1-1 1A17 17 0 0 1 3 4a1 1 0 0 1 1-1h3.5a1 1 0 0 1 1 1c0 1.25.2 2.45.57 3.6a1 1 0 0 1-.25 1z" fill="#1b5c98"/></svg>
  </div></div>
  <div class="abs f-node" style="left:546px"><div class="f-node-inner">
    <svg width="30" height="30" viewBox="0 0 24 24" aria-label="location"><path d="M12 2a7 7 0 0 0-7 7c0 5.2 7 13 7 13s7-7.8 7-13a7 7 0 0 0-7-7zm0 9.5A2.5 2.5 0 1 1 12 6.5a2.5 2.5 0 0 1 0 5z" fill="#1b5c98"/></svg>
  </div></div>
  <div class="abs f-node" style="left:905px"><div class="f-node-inner">
    <svg width="30" height="30" viewBox="0 0 24 24" aria-label="email"><path d="M3 5h18v14H3z" fill="#1b5c98"/><path d="M3 5l9 8 9-8" stroke="#6fa31a" stroke-width="1.6" fill="none"/></svg>
  </div></div>

  <p class="abs f-text" style="left:139px;width:200px">123 456 7890</p>
  <p class="abs f-text" style="left:440px;width:320px">Lorem Ipsum is simply dummy text of the printing and typesetting.</p>
  <p class="abs f-text" style="left:819px;width:280px">info@halden-consulting.com</p>
  <p class="abs center copyright">©halden consulting- 2018. All Rights Reserved.</p>

</div>
</body>
</html>
```